UHT milk packaging Design, (Package Design and Outer Carton Design)

Create a Packaging Design
We would like to you to design a UHT milk packaging. We would need our brand logo on the box (Corvin or Brisko). At present, we do not have a logo design, only the brand name. The Name of the product will be "Full Cream Milk", "Skim Milk", "Lite Milk"

We use Sorvo Kase packaging,
Dimensions of 1L product: 90mm*58mm*195mm
Dimensions of 250ml product: 63mm*40mm*106mm

It should also include:
Barcode placeholder
Area for ingredients
1L and 250ml

Upload files are photoes of other Sorvo Kase packaging

The final design should communicate:
Freshness
Healthy
Modern
Striking

Subsequently, we also have other products packaging that need to be designed, such as muesli, meat, etc

Target Market(s)

family consumption

Font styles to use
Decorative

Requirements
Must have
• Our brand logo (BRISKO);
• Make people feel fresh and healthy
Nice to have
• Bright colors;
• Attractive picture

```html
<!DOCTYPE html>
<html lang="en">
<head>
<meta charset="utf-8">
<title>Corvin UHT Milk Cartons</title>
<link href="https://fonts.googleapis.com/css2?family=Open+Sans:wght@400;600;700&display=swap" rel="stylesheet">
<style>
  :root {
    --bg: #ffffff;
    --ink: #2b2b2b;
    --navy: #1c1f6e;
    --full-cream: #d7141b;
    --full-cream-soft: #eb8a8d;
    --skim: #e0619b;
    --skim-soft: #f0a9c9;
    --panel: #ffffff;
    --edge: #e4e4e4;
  }
  * { box-sizing: border-box; margin: 0; padding: 0; }
  html, body {
    width: 1200px; height: 900px; overflow: hidden;
    background: var(--bg);
    font-family: "Open Sans", Arial, sans-serif;
    color: var(--ink);
  }
  .lineup {
    position: absolute; left: 49px; top: 100px;
    display: flex; gap: 40px;
  }
  .carton { display: flex; height: 700px; --brand: var(--full-cream); --brand-soft: var(--full-cream-soft); }
  .carton--skim { --brand: var(--skim); --brand-soft: var(--skim-soft); }

  /* Side panel */
  .side {
    position: relative; width: 208px; height: 700px;
    background: var(--panel); border: 1px solid var(--edge); border-right: none;
    overflow: hidden;
  }
  .side__band { height: 46px; background: var(--brand); }
  .side__body { padding: 18px 12px 0 12px; font-size: 7.5px; line-height: 1.45; }
  .side__title { color: var(--brand); font-weight: 700; font-size: 17px; line-height: 1.1; margin-bottom: 14px; }
  .side__heading { font-weight: 700; font-size: 8.5px; text-align: center; margin-bottom: 3px; }
  .side__storage { text-align: center; margin-bottom: 22px; }
  .side__label { font-weight: 700; font-size: 8.5px; margin-bottom: 12px; }
  .side__highlights { margin-bottom: 26px; }
  .side__address { margin-bottom: 14px; }
  .side__marks { display: flex; align-items: center; gap: 12px; margin-top: 20px; }
  .cert-badge { width: 62px; height: 44px; border: 1.5px solid var(--ink); border-radius: 4px; }
  .recycle-icon { width: 30px; height: 30px; }

  /* Front panel */
  .front {
    position: relative; width: 323px; height: 700px;
    background: var(--panel); border: 1px solid var(--edge);
    overflow: hidden;
  }
  .front__art { position: absolute; inset: 0; }
  .front__title {
    position: absolute; top: 52px; left: 0; width: 100%;
    text-align: center; color: #fff; font-weight: 600; font-size: 29px;
  }
  .brand-name {
    position: absolute; top: 182px; left: 0; width: 100%;
    display: flex; justify-content: center; align-items: center;
    color: var(--navy); font-weight: 700; font-size: 54px; line-height: 1;
  }
  .cow-illustration {
    position: absolute; left: 22px; top: 320px; width: 290px; height: 300px;
    background: radial-gradient(ellipse at 50% 55%, var(--brand-soft) 0%, rgba(255,255,255,0) 70%);
    border-radius: 8px;
  }
  .volume-badge {
    position: absolute; right: 26px; top: 636px; width: 34px; height: 40px;
    background: var(--brand); color: #fff; border-radius: 4px 4px 3px 3px;
    font-weight: 700; font-size: 13px; display: flex; align-items: flex-end; justify-content: center;
    padding-bottom: 6px;
  }
</style>
</head>
<body>
<main class="lineup">

  <section class="carton carton--full-cream">
    <div class="side">
      <div class="side__band"></div>
      <div class="side__body">
        <p class="side__title">Full Cream Milk</p>
        <p class="side__heading">Storage information</p>
        <p class="side__storage">Store in a cool, dry place away from sunlight. Once opened, keep refrigerated between 1-4°C and consume within 5 days.</p>
        <p class="side__label">HIGHLIGHTS</p>
        <p class="side__highlights">Fresh milk from grass-fed herds, gently heat treated to keep its natural goodness. Rich in calcium and protein for the whole family. Enjoy it chilled, in tea and coffee, or over your morning cereal.</p>
        <p class="side__address">Manufactured by: Larkfield Dairy Co<br>8 Riverbend Road,<br>Fernvale 3712<br>Victoria, Australia.<br>Est No 7381</p>
        <p class="side__address">Packed For: COMPANY XXXX XXX<br>42 Harbour Lane, Sydney 2000, NSW, Australia<br>Website: XXX.XXXX.XXX<br>Phone: XX XXXX XXX</p>
        <div class="side__marks">
          <div class="cert-badge"></div>
          <svg class="recycle-icon" viewBox="0 0 30 30" aria-hidden="true">
            <g fill="none" stroke="#2b2b2b" stroke-width="2.4" stroke-linejoin="round">
              <path d="M15 4 L26 24 L4 24 Z"/>
            </g>
            <g fill="#2b2b2b">
              <path d="M19 9 L23 12 L18 14 Z"/>
              <path d="M17 21 L17 27 L12 24 Z"/>
              <path d="M6 16 L9 12 L11 17 Z"/>
            </g>
          </svg>
        </div>
      </div>
    </div>
    <div class="front">
      <svg class="front__art" viewBox="0 0 323 700" aria-hidden="true">
        <path d="M0 0 H323 V150 Q180 130 0 175 Z" fill="var(--brand)"/>
        <g fill="none" stroke="var(--brand)" stroke-linecap="round">
          <path d="M110 178 Q190 150 280 145" stroke-width="4"/>
          <path d="M130 190 Q200 168 260 162" stroke-width="2"/>
          <path d="M20 328 Q150 285 300 272" stroke-width="5"/>
          <path d="M60 342 Q170 308 280 296" stroke-width="2.5"/>
          <path d="M-10 640 Q90 660 200 700" stroke-width="5"/>
          <path d="M10 660 Q80 672 150 700" stroke-width="2.5"/>
        </g>
      </svg>
      <h1 class="front__title">Full Cream Milk</h1>
      <div class="brand-name"><span>Corvin</span></div>
      <div class="cow-illustration" role="img" aria-label="Line illustration of two spotted dairy cows in the carton colour, one grazing behind and one standing in front"></div>
      <div class="volume-badge">1L</div>
    </div>
  </section>

  <section class="carton carton--skim">
    <div class="side">
      <div class="side__band"></div>
      <div class="side__body">
        <p class="side__title">Skim Milk</p>
        <p class="side__heading">Storage information</p>
        <p class="side__storage">Store in a cool, dry place away from sunlight. Once opened, keep refrigerated between 1-4°C and consume within 5 days.</p>
        <p class="side__label">HIGHLIGHTS</p>
        <p class="side__highlights">Fresh milk from grass-fed herds, gently heat treated to keep its natural goodness. Rich in calcium and protein for the whole family. Enjoy it chilled, in tea and coffee, or over your morning cereal.</p>
        <p class="side__address">Manufactured by: Larkfield Dairy Co<br>8 Riverbend Road,<br>Fernvale 3712<br>Victoria, Australia.<br>Est No 7381</p>
        <p class="side__address">Packed For: COMPANY XXXX XXX<br>42 Harbour Lane, Sydney 2000, NSW, Australia<br>Website: XXX.XXXX.XXX<br>Phone: XX XXXX XXX</p>
        <div class="side__marks">
          <div class="cert-badge"></div>
          <svg class="recycle-icon" viewBox="0 0 30 30" aria-hidden="true">
            <g fill="none" stroke="#2b2b2b" stroke-width="2.4" stroke-linejoin="round">
              <path d="M15 4 L26 24 L4 24 Z"/>
            </g>
            <g fill="#2b2b2b">
              <path d="M19 9 L23 12 L18 14 Z"/>
              <path d="M17 21 L17 27 L12 24 Z"/>
              <path d="M6 16 L9 12 L11 17 Z"/>
            </g>
          </svg>
        </div>
      </div>
    </div>
    <div class="front">
      <svg class="front__art" viewBox="0 0 323 700" aria-hidden="true">
        <path d="M0 0 H323 V150 Q180 130 0 175 Z" fill="var(--brand)"/>
        <g fill="none" stroke="var(--brand)" stroke-linecap="round">
          <path d="M110 178 Q190 150 280 145" stroke-width="4"/>
          <path d="M130 190 Q200 168 260 162" stroke-width="2"/>
          <path d="M20 328 Q150 285 300 272" stroke-width="5"/>
          <path d="M60 342 Q170 308 280 296" stroke-width="2.5"/>
          <path d="M-10 640 Q90 660 200 700" stroke-width="5"/>
          <path d="M10 660 Q80 672 150 700" stroke-width="2.5"/>
        </g>
      </svg>
      <h1 class="front__title">Skim Milk</h1>
      <div class="brand-name"><span>Corvin</span></div>
      <div class="cow-illustration" role="img" aria-label="Line illustration of two spotted dairy cows in the carton colour, one grazing behind and one standing in front"></div>
      <div class="volume-badge">1L</div>
    </div>
  </section>

</main>
</body>
</html>
```